Professional and creatice Life Coach - Business Card design

I just relaunched my website and now i a need a correspoonding business card for my task as life coach. My website is www.tbalrond.com as reference. The compass is kind of a symbol for my work, as I help people navigate through their challenging phases in life. The business card should be colorful, but not too playful as I also adress business people. So it sould be creative, but professional (also to suport my other business as Management Consultant)

Target Market(s)

People who want to get teir problems resolved, in business, partnership and other personal realms

Industry/Entity Type

Life Coaching

Contact Information for Business Card

Front side should include Name, Phone number, Email, Website and address

Font styles to use
Sans Serif

Colors
add136

Requirements
Must have
• "Mag. Leopold Brantner" -> Name
"Energetische Praxis" -> Jobtitle (describing my profession as life coach)
colours and style should match my website www.tbalrond.com
Nice to have
• a compass as a symbol

```html
<!DOCTYPE html>
<html lang="de">
<head>
<meta charset="utf-8">
<title>Leopold Brantner – Visitenkarte</title>
<link rel="stylesheet" href="https://fonts.googleapis.com/css2?family=Lato:wght@300;400;700&display=swap">
<style>
  :root {
    --stage: #bcbdc0;
    --paper: #ffffff;
    --lime: #add136;
    --lime-pale: #dfeab7;
    --lime-faint: #cddd9f;
    --ink: #000000;
  }
  html, body { margin: 0; padding: 0; overflow: hidden; }
  body {
    width: 1022px; height: 1200px;
    background: var(--stage);
    position: relative;
    font-family: 'Lato', sans-serif;
    color: var(--ink);
  }
  .card {
    position: absolute; left: 23px; width: 976px; height: 558px;
    background: var(--paper);
  }
  .card--front { top: 23px; }
  .card--back { top: 619px; }

  .front-field {
    position: absolute; left: 38px; top: 38px; width: 899px; height: 477px;
    background: var(--lime-pale); overflow: hidden;
  }
  .front-field__emblem {
    position: absolute; left: 687px; top: 0; width: 212px; height: 212px;
  }
  .name-marker {
    position: absolute; left: 0; top: 61px; width: 39px; height: 63px;
    background: var(--lime);
    border-top: 1.5px solid var(--ink); border-bottom: 1.5px solid var(--ink);
  }
  .identity { position: absolute; left: 77px; top: 55px; margin: 0; }
  .identity__name { margin: 0; font-weight: 700; font-size: 34px; line-height: 40px; letter-spacing: -0.3px; }
  .identity__title { margin: 0; font-weight: 400; font-size: 23px; line-height: 28px; }

  .contact {
    position: absolute; left: 242px; top: 310px; width: 657px; height: 148px;
    background: var(--lime);
    border-top: 1.5px solid var(--ink); border-bottom: 1.5px solid var(--ink);
    box-sizing: border-box; padding: 9px 0 0 16px;
    margin: 0; list-style: none;
    font-size: 26px; line-height: 33px;
  }
  .contact__label { font-weight: 300; }
  .contact__value { font-weight: 400; }

  .back-field {
    position: absolute; left: 38px; top: 44px; width: 899px; height: 474px;
    background: var(--lime);
    border-top: 1.5px solid var(--ink); border-bottom: 1.5px solid var(--ink);
    box-sizing: border-box;
    display: flex; align-items: center; justify-content: center; gap: 14px;
  }
  .brand-dot { width: 22px; height: 22px; border-radius: 50%; background: var(--ink); }
  .brand-name { font-weight: 700; font-size: 30px; }
</style>
</head>
<body>
  <section class="card card--front">
    <div class="front-field">
      <svg class="front-field__emblem" viewBox="0 0 212 212" role="img" aria-label="Faint decorative circle">
        <circle cx="168" cy="106" r="104" fill="none" stroke="var(--lime-faint)" stroke-width="3"/>
      </svg>
      <div class="name-marker"></div>
      <header class="identity">
        <h1 class="identity__name">Mag. Leopold Brantner</h1>
        <p class="identity__title">ENERGETISCHE PRAXIS</p>
      </header>
      <ul class="contact">
        <li><span class="contact__label">Address:</span> <span class="contact__value">Lindenweg 12, 5020 Salzburg, Österreich</span></li>
        <li><span class="contact__label">Phone:</span> <span class="contact__value">+43 660 5558142</span></li>
        <li><span class="contact__label">e-mail:</span> <span class="contact__value">leopold@brantner.co</span></li>
        <li><span class="contact__label">website:</span> <span class="contact__value">www.tbalrond.com</span></li>
      </ul>
    </div>
  </section>

  <section class="card card--back">
    <div class="back-field">
      <span class="brand-dot"></span>
      <span class="brand-name">Leopold Brantner</span>
    </div>
  </section>
</body>
</html>
```